TIME BAR Design Project

DESIGN: TIME LAPSE BAR

We are looking for a fresh design for a time lapse bar which would appear on screen during an exercise video.

Please see a quick example attached. We would like it to be created in Photoshop or Illustrator, in layers. ( no after effects please).

We need a layer that would move to indicate the time passing.

We would like to manipulate the time as needed for various pieces.
Updates

Quick update:
please note the current bar in the sample picts was done in-house and is only intended to be a guide.  The bar does not have to resemble the sample. Thanks.

Target Market(s)

male /female 25-65 60% women.

Requirements
Must have
• Created in Photoshop or Illustrator.

Minimum 300DPI.

Please see that there is needs to be a place for the name of each exercise - this can appear and then fade out.
Nice to have
• -bar should match the mood of the set and colors.( see picts).

-bar CAN BE see-through so that the body's are seen behind it.
Should not have
• too high tech or masculine

too feminine

```html
<!DOCTYPE html>
<html lang="en">
<head>
<meta charset="utf-8">
<title>Time Lapse Bar</title>
<link href="https://fonts.googleapis.com/css2?family=Roboto+Condensed:wght@700&display=swap" rel="stylesheet">
<style>
  :root {
    --wall: #efe8dc;
    --wall-warm: #e6d6bd;
    --floor: #d7b58b;
    --floor-deep: #c79d6c;
    --fade-white: #ffffff;
    --track-dark: #2a2f36;
    --track-edge: #0f1215;
    --fill-light: #7fc4ef;
    --fill-mid: #2f8fd0;
    --fill-deep: #1a5e9c;
    --knob: #f4f5f6;
    --knob-edge: #9aa3ab;
    --title-ink: #2b2b2b;
    --time-blue: #1f6fb4;
  }
  html, body {
    margin: 0;
    padding: 0;
    width: 1200px;
    height: 673px;
    overflow: hidden;
    background: var(--wall);
  }
  .screen {
    position: relative;
    width: 1200px;
    height: 673px;
    overflow: hidden;
  }
  .video-frame {
    position: absolute;
    inset: 0;
    background:
      linear-gradient(180deg, var(--wall) 0%, var(--wall-warm) 48%, var(--floor) 62%, var(--floor-deep) 100%);
  }
  .bottom-fade {
    position: absolute;
    left: 0;
    right: 0;
    bottom: 0;
    height: 150px;
    background: linear-gradient(180deg, rgba(255,255,255,0) 0%, rgba(255,255,255,0.78) 45%, rgba(255,255,255,0.95) 100%);
  }
  .time-bar {
    position: absolute;
    left: 249px;
    top: 566px;
    width: 653px;
  }
  .track {
    position: relative;
    height: 19px;
    border-radius: 10px;
    background: linear-gradient(180deg, #4a5058 0%, var(--track-dark) 55%, var(--track-edge) 100%);
    box-shadow: inset 0 1px 2px rgba(0,0,0,0.6);
  }
  .progress {
    position: absolute;
    left: 2px;
    top: 2px;
    bottom: 2px;
    width: 441px;
    border-radius: 8px 0 0 8px;
    background: linear-gradient(180deg, var(--fill-light) 0%, var(--fill-mid) 50%, var(--fill-deep) 100%);
  }
  .knob {
    position: absolute;
    left: 434px;
    top: -10px;
    width: 19px;
    height: 38px;
    border-radius: 3px;
    background: linear-gradient(90deg, #ffffff 0%, var(--knob) 55%, #d3d8dc 100%);
    border: 1px solid var(--knob-edge);
    box-sizing: border-box;
  }
  .labels {
    display: flex;
    justify-content: space-between;
    align-items: baseline;
    margin-top: 14px;
    font-family: "Roboto Condensed", "Arial Narrow", sans-serif;
    font-weight: 700;
    font-size: 21px;
    letter-spacing: 0.3px;
  }
  .exercise-name {
    color: var(--title-ink);
  }
  .elapsed {
    color: var(--time-blue);
  }
  .total {
    color: var(--title-ink);
  }
</style>
</head>
<body>
  <div class="screen">
    <div class="video-frame" role="img" aria-label="Exercise video scene: two instructors working out in a bright studio with a wooden floor"></div>
    <div class="bottom-fade"></div>
    <div class="time-bar">
      <div class="track">
        <div class="progress"></div>
        <div class="knob"></div>
      </div>
      <div class="labels">
        <span class="exercise-name">A WORKOUT TITLE</span>
        <span class="timecode"><span class="elapsed">14:29:19</span><span class="total"> / 25:59:00</span></span>
      </div>
    </div>
  </div>
</body>
</html>
```